Consultant company (start up) needs a bold, yet simple web design

We need a we design for "K7P Ledger & Consulting". As our name implies we are a consultant firm helping companies with public sector business (tenders), but also helping the buyer side. We provide market research and reports, advice (legal and business) and hands-on-help with tender applications (projectleader; analysing critiera and texts, document reviews, etc). We have a rather uniqe position in our market with our mixed competences of branding and market communication, formal management systems, and public tenders.

We have a strong drive to make tender business simple for our clients: we will take care of the complicated!

We want our web design to be bold, yet clean and simple, communicating:

Competence; Commitment, Simplicity (for the customer).
Updates

Reason: For different reasons our web project was put on hold/was delayed a few days. As of today we are kicking life into it again, and expect to come back with feedback on designs in the next days. Best regards, Mattias

Target Market(s)

We primarily help companies aiming for public contracts.

Industry/Entity Type

Business Consultant

Contact Information for Business Card

Company logo; First name, Last name, Titel, webadress; personal e-mail
Maybe: a motto like "Offentliga affärer. Enklare" ("Public business. Made simple.")

Coding

Coded - Design and coding required

Font styles to use
Sans Serif

Colors

Designer to choose colors to be used in the design.

Requirements
Must have
• Dual language (Swedish and English)
• Responsive design, many people will view our webpage on their phone or tavlo.
• We want to make our position clear, stating what distinguishes us from "the rest of the pack" in maybe with on the starting page.
• [Will update brief; need to think this through]
Nice to have
• We have our logo in three colours. Green is our first. We are not yet sure why we have the different colurs. Maybe (just maybe!) the different colours can be put to use?
• We need help with the choice of images.
Should not have
• Never boring.

```html
<!DOCTYPE html>
<html lang="sv">
<head>
<meta charset="utf-8">
<title>K7P Ledger &amp; Consulting</title>
<link rel="stylesheet" href="https://fonts.googleapis.com/css2?family=Montserrat:wght@400;600;700&family=Open+Sans:wght@400;600&display=swap">
<style>
:root{
  --green:#6fa53c;
  --green-bright:#79b041;
  --green-soft:#91c25d;
  --dark:#333534;
  --darker:#232524;
  --ink:#3a3a3a;
  --muted:#777;
  --light:#f1f1f1;
  --white:#fff;
  --suit:#24324a;
  --shirt:#dfe5ec;
  --skin:#c9a083;
  --desk:#eef1f4;
}
*{box-sizing:border-box;margin:0;padding:0}
html,body{width:1200px;height:5244px;overflow:hidden}
body{font-family:"Open Sans",Arial,sans-serif;color:var(--ink);background:var(--white);position:relative}
h1,h2,h3,h4,.brand,.btn,.nav a{font-family:"Montserrat",Arial,sans-serif}
section,header,footer{position:relative;width:1200px;overflow:hidden}

/* navigation */
.site-nav{height:77px;display:flex}
.brand-area{width:385px;background:var(--white);display:flex;align-items:center;padding-left:40px;gap:12px}
.brand-mark{width:34px;height:34px;border-radius:50%;background:var(--green)}
.brand{font-weight:700;font-size:18px;color:var(--green)}
.nav{flex:1;background:var(--green-bright);display:flex;align-items:center;padding-left:20px;gap:38px}
.nav a{color:var(--white);text-decoration:none;font-size:14px;font-weight:600}
.nav .social{display:flex;gap:12px;margin-left:8px}
.nav .social span{width:16px;height:16px;border-radius:50%;background:rgba(255,255,255,.85)}

/* photo fills */
.photo-office{background:
  radial-gradient(ellipse 22% 30% at 28% 30%, rgba(214,178,150,.75), transparent 70%),
  radial-gradient(ellipse 30% 45% at 72% 40%, rgba(30,44,66,.95), transparent 75%),
  radial-gradient(ellipse 35% 25% at 35% 85%, rgba(245,247,250,.9), transparent 70%),
  radial-gradient(ellipse 25% 40% at 95% 70%, rgba(18,26,40,.95), transparent 70%),
  linear-gradient(100deg,#d9dde1 0%,#aeb7c1 30%,#5b6c82 58%,#223049 82%,#1a2436 100%)}
.photo-desk{background:
  radial-gradient(ellipse 40% 30% at 35% 70%, rgba(250,251,252,.95), transparent 70%),
  radial-gradient(ellipse 20% 30% at 60% 45%, rgba(110,150,200,.7), transparent 70%),
  radial-gradient(ellipse 25% 40% at 15% 25%, rgba(70,80,95,.8), transparent 70%),
  radial-gradient(ellipse 25% 40% at 90% 25%, rgba(50,60,75,.85), transparent 70%),
  linear-gradient(160deg,#c5ccd3,#e8ecef 50%,#aab3bc)}
.photo-meeting{background:
  radial-gradient(ellipse 18% 25% at 30% 22%, rgba(205,165,135,.8), transparent 70%),
  radial-gradient(ellipse 16% 22% at 72% 30%, rgba(200,160,130,.8), transparent 70%),
  radial-gradient(ellipse 30% 40% at 20% 70%, rgba(90,130,185,.85), transparent 70%),
  radial-gradient(ellipse 30% 40% at 65% 75%, rgba(240,242,245,.95), transparent 70%),
  radial-gradient(ellipse 25% 45% at 92% 60%, rgba(40,45,55,.85), transparent 70%),
  linear-gradient(135deg,#b8c3ce,#8d9aa8 50%,#d5dbe0)}
.photo-dim{background:
  radial-gradient(ellipse 30% 70% at 85% 55%, rgba(85,92,100,.9), transparent 70%),
  radial-gradient(ellipse 25% 40% at 60% 65%, rgba(70,76,82,.7), transparent 70%),
  radial-gradient(ellipse 50% 30% at 50% 100%, rgba(20,22,24,.9), transparent 70%),
  linear-gradient(90deg,#2b3034 0%,#3c4349 40%,#4b535a 65%,#33393e 100%)}
.photo-papers{background:
  radial-gradient(ellipse 30% 40% at 20% 60%, rgba(140,150,160,.55), transparent 70%),
  radial-gradient(ellipse 30% 50% at 85% 40%, rgba(110,118,126,.5), transparent 70%),
  linear-gradient(120deg,#3a4146,#565f66 50%,#2f353a)}
.map{background:
  radial-gradient(ellipse 18% 40% at 10% 70%, rgba(120,170,215,.85), transparent 70%),
  radial-gradient(ellipse 14% 30% at 55% 90%, rgba(120,170,215,.8), transparent 70%),
  radial-gradient(ellipse 22% 45% at 35% 35%, rgba(200,222,165,.9), transparent 70%),
  radial-gradient(ellipse 20% 40% at 80% 40%, rgba(206,226,170,.9), transparent 70%),
  radial-gradient(ellipse 15% 30% at 65% 20%, rgba(232,190,190,.8), transparent 70%),
  linear-gradient(120deg,#ece3cc,#e6dcc4 50%,#efe6d2)}

/* hero */
.hero{height:588px;color:var(--white);text-align:center}
.hero .photo{position:absolute;inset:0}
.hero .veil{position:absolute;inset:0;background:rgba(20,25,30,.18)}
.hero-name{position:absolute;top:165px;left:0;right:0;font-family:"Montserrat",sans-serif;font-weight:700;font-size:64px;color:var(--green-bright)}
.hero-tag{position:absolute;top:330px;left:0;right:0;font-size:17px;letter-spacing:10px;font-family:"Montserrat",sans-serif}
.scroll{position:absolute;top:420px;left:0;right:0;font-size:12px}
.scroll-btn{position:absolute;top:455px;left:575px;width:50px;height:50px;border:2px solid var(--white);border-radius:50%}

/* features */
.features{height:553px;background:var(--green-bright);color:var(--white)}
.section-title{font-weight:700;font-size:26px;letter-spacing:2px;text-align:center}
.features .section-title{position:absolute;top:118px;left:0;right:0}
.feature{position:absolute;top:223px;width:200px;text-align:center}
.feature .icon{width:84px;height:84px;margin:0 auto;border-radius:50%;background:var(--green-soft);display:flex;align-items:center;justify-content:center}
.feature h3{font-size:15px;margin-top:28px;letter-spacing:1px}
.feature p{font-size:12px;line-height:1.6;margin-top:14px}

/* split rows */
.split{display:flex}
.split .panel{width:600px;position:relative}
.research{height:332px}
.research .panel.text{background:var(--dark);color:var(--white);padding:55px 70px 0 160px}
.consulting{height:361px}
.consulting .panel.text{background:var(--light);padding:60px 120px 0 60px}
.panel h3{font-size:16px;letter-spacing:1px;margin-bottom:22px}
.panel p{font-size:12.5px;line-height:1.75;margin-bottom:10px}
.consulting .panel p{color:var(--muted)}
.btn{display:inline-block;background:var(--green-bright);color:var(--white);font-size:11px;font-weight:600;padding:8px 22px;margin-top:10px}

/* services */
.services{height:767px;text-align:center}
.services .section-title{position:absolute;top:78px;left:0;right:0;color:var(--ink)}
.services .sub{position:absolute;top:218px;left:0;right:0;font-size:22px;color:#444}
.service{position:absolute;top:305px;width:205px}
.service .thumb{height:210px}
.service h4{font-size:15px;margin-top:34px}
.service p{font-size:12px;line-height:1.65;color:var(--muted);margin-top:12px;text-align:left}

/* quotes band */
.quotes{height:269px;background:var(--green-bright);color:var(--white)}
.quote{position:absolute;top:88px;width:440px;display:flex;gap:22px}
.quote svg{flex:none}
.quote p{font-size:13px;line-height:1.7}

/* skills */
.skills{height:630px;color:var(--white)}
.skills .photo{position:absolute;inset:0}
.skills .body{position:absolute;top:150px;left:165px;width:340px}
.skills h3{font-size:16px;letter-spacing:1px}
.skills p{font-size:12.5px;line-height:1.7;margin-top:18px}
.bar{height:24px;background:var(--green-bright);margin-top:14px;font-family:"Montserrat",sans-serif;font-size:11px;font-weight:700;padding:5px 10px}

/* team */
.team{height:711px;text-align:center}
.team .section-title{position:absolute;top:100px;left:0;right:0;color:var(--ink)}
.team .sub{position:absolute;top:228px;left:0;right:0;font-size:20px}
.member{position:absolute;top:308px;width:200px}
.member .portrait{height:280px}
.member h4{font-size:14px;color:var(--green-bright);margin-top:18px}
.member span{font-size:11px;color:var(--muted)}

/* map */
.map{height:262px}

/* contact */
.contact{height:623px;color:var(--white)}
.contact .photo{position:absolute;inset:0}
.contact .veil{position:absolute;inset:0;background:rgba(15,18,20,.35)}
.contact .section-title{position:absolute;top:122px;left:0;right:0;font-size:44px;font-weight:600;letter-spacing:1px}
.field{position:absolute;border:1px solid rgba(255,255,255,.6);font-size:11px;padding:10px 12px;color:rgba(255,255,255,.8)}
.submit{position:absolute;top:507px;left:515px;width:170px;height:42px;background:var(--green-bright);font-family:"Montserrat",sans-serif;font-weight:700;font-size:15px;display:flex;align-items:center;justify-content:center}

/* footer */
.site-footer{height:71px;background:var(--darker);color:#aaa;display:flex;align-items:center;justify-content:space-between;padding:0 40px 0 165px;font-size:11px}
.site-footer .brand{font-size:16px}
</style>
</head>
<body>

<header class="site-nav">
  <div class="brand-area"><span class="brand-mark"></span><span class="brand">K7P Ledger &amp; Consulting</span></div>
  <nav class="nav">
    <a href="#">Home</a><a href="#">About</a><a href="#">Services</a><a href="#">Our Mission</a><a href="#">Why Us</a><a href="#">Contact us</a>
    <div class="social"><span></span><span></span><span></span><span></span></div>
  </nav>
</header>

<section class="hero">
  <div class="photo photo-office" role="img" aria-label="Business people in suits working together at a desk with documents"></div>
  <div class="veil"></div>
  <div class="hero-name">K7P Ledger &amp; Consulting</div>
  <div class="hero-tag">PUBLIC BUSINESS. MADE SIMPLE.</div>
  <div class="scroll">Scroll down</div>
  <div class="scroll-btn"><svg width="46" height="46" viewBox="0 0 46 46"><polyline points="17,20 23,26 29,20" fill="none" stroke="#fff" stroke-width="2"/></svg></div>
</section>

<section class="features">
  <h2 class="section-title">HÄST DENNA ANNAT ANNAN DÄRMED OSS</h2>
  <div class="feature" style="left:180px">
    <div class="icon"><svg width="30" height="30" viewBox="0 0 30 30" fill="none" stroke="#fff" stroke-width="2"><rect x="3" y="5" width="20" height="20"/><path d="M12 18l2-5 11-11 3 3-11 11z"/></svg></div>
    <h3>FEATURE ONE</h3><p>Snabb hjälp med anbud, tydliga krav och enkla steg för alla kunder.</p>
  </div>
  <div class="feature" style="left:415px">
    <div class="icon"><svg width="30" height="30" viewBox="0 0 30 30" fill="none" stroke="#fff" stroke-width="2"><path d="M20 4l6 6-14 14H6v-6z"/><line x1="4" y1="27" x2="26" y2="27"/></svg></div>
    <h3>FEATURE TWO</h3><p>Snabb hjälp med anbud, tydliga krav och enkla steg för alla kunder.</p>
  </div>
  <div class="feature" style="left:645px">
    <div class="icon"><svg width="30" height="30" viewBox="0 0 30 30" fill="none" stroke="#fff" stroke-width="2.4"><circle cx="12" cy="12" r="8"/><line x1="18" y1="18" x2="27" y2="27"/></svg></div>
    <h3>FEATURE THREE</h3><p>Snabb hjälp med anbud, tydliga krav och enkla steg för alla kunder.</p>
  </div>
  <div class="feature" style="left:870px">
    <div class="icon"><svg width="30" height="30" viewBox="0 0 30 30" fill="none" stroke="#fff" stroke-width="2"><circle cx="15" cy="14" r="10"/><path d="M8 21l-3 6 7-3"/></svg></div>
    <h3>FEATURE FOUR</h3><p>Snabb hjälp med anbud, tydliga krav och enkla steg för alla kunder.</p>
  </div>
</section>

<section class="split research">
  <div class="panel text">
    <h3>RESEARCH</h3>
    <p>Vi tar fram marknadsanalyser och rapporter som visar var affärerna finns och hur ni når dem. Vår metod är enkel, snabb och tydlig för varje kund.</p>
    <p>Vi läser underlag, granskar krav och ger råd som gör anbudet starkare.</p>
    <span class="btn">READ MORE</span>
  </div>
  <div class="panel photo-desk" role="img" aria-label="Hands reviewing charts and papers on a meeting table"></div>
</section>

<section class="split consulting">
  <div class="panel photo-meeting" role="img" aria-label="Team of consultants in discussion around a table"></div>
  <div class="panel text">
    <h3>CONSULTING</h3>
    <p>Vi leder anbudsarbetet från start till inlämning, granskar dokument och tolkar kriterier. Ni får en partner som tar hand om det komplicerade.</p>
    <p>Juridiska och affärsmässiga råd samlat hos ett team.</p>
    <span class="btn">READ MORE</span>
  </div>
</section>

<section class="services">
  <h2 class="section-title">HÄST DENNA ANNAT ANNAN DÄRMED OSS</h2>
  <p class="sub">Tidigare flera sig det lax faktor dock och greda, vad söka precis</p>
  <div class="service" style="left:158px"><div class="thumb photo-meeting" role="img" aria-label="Woman working at a laptop"></div><h4>HÄST DENNA</h4><p>Vi hjälper köpare och säljare att mötas i offentliga affärer med tydliga underlag och trygg process.</p></div>
  <div class="service" style="left:385px"><div class="thumb photo-desk" role="img" aria-label="Pen pointing at printed business charts"></div><h4>HÄST DENNA</h4><p>Vi hjälper köpare och säljare att mötas i offentliga affärer med tydliga underlag och trygg process.</p></div>
  <div class="service" style="left:612px"><div class="thumb photo-office" role="img" aria-label="Laptop and documents on an office desk"></div><h4>HÄST DENNA</h4><p>Vi hjälper köpare och säljare att mötas i offentliga affärer med tydliga underlag och trygg process.</p></div>
  <div class="service" style="left:840px"><div class="thumb" role="img" aria-label="Smiling senior businessman in a suit" style="background:radial-gradient(ellipse 35% 30% at 55% 35%, rgba(205,165,135,.85), transparent 70%),linear-gradient(180deg,#eef0f2 0%,#dfe3e7 45%,#2c3a52 80%,#1f2a3d 100%)"></div><h4>HÄST DENNA</h4><p>Vi hjälper köpare och säljare att mötas i offentliga affärer med tydliga underlag och trygg process.</p></div>
</section>

<section class="quotes">
  <div class="quote" style="left:160px">
    <svg width="46" height="46" viewBox="0 0 46 46" fill="none" stroke="#fff" stroke-width="3"><rect x="3" y="8" width="32" height="34"/><path d="M18 30l3-8 18-18 5 5-18 18z"/></svg>
    <p>Hast denna annat annan därmed oss finns ingenting så enkelt som ett väl förberett anbud. Vi gör processen tydlig från början.</p>
  </div>
  <div class="quote" style="left:620px">
    <svg width="46" height="46" viewBox="0 0 46 46" fill="none" stroke="#fff" stroke-width="3"><rect x="3" y="8" width="32" height="34"/><path d="M18 30l3-8 18-18 5 5-18 18z"/></svg>
    <p>Hast denna annat annan därmed oss finns ingenting så enkelt som ett väl förberett anbud. Vi gör processen tydlig från början.</p>
  </div>
</section>

<section class="skills">
  <div class="photo photo-dim" role="img" aria-label="Businessman with folded arms in a dim meeting room"></div>
  <div class="body">
    <h3>HÄST DENNA ANNAT</h3>
    <p>Vi kombinerar varumärke, ledningssystem och offentlig upphandling i ett och samma team, så att ni får hela bilden.</p>
    <div class="bar" style="width:280px;margin-top:30px">RESEARCH</div>
    <div class="bar" style="width:300px">HIGH QUALITY WORK</div>
    <div class="bar" style="width:330px">CONSULTING</div>
  </div>
</section>

<section class="team">
  <h2 class="section-title">OUR TEAM</h2>
  <p class="sub">sales long tail influencer pitch release niche market.</p>
  <div class="member" style="left:165px"><div class="portrait" role="img" aria-label="Portrait of Erik Lund" style="background:radial-gradient(ellipse 32% 22% at 50% 32%, rgba(200,155,125,.9), transparent 70%),linear-gradient(180deg,#f4f4f4 0%,#e9e9e9 50%,#3a3a40 72%,#26262c 100%)"></div><h4>ERIK LUND</h4><span>CEO</span></div>
  <div class="member" style="left:388px"><div class="portrait" role="img" aria-label="Portrait of Anna Berg" style="background:radial-gradient(ellipse 42% 30% at 50% 32%, rgba(222,190,140,.9), transparent 72%),linear-gradient(180deg,#f5f5f5 0%,#ececec 50%,#2e2e34 75%,#222 100%)"></div><h4>ANNA BERG</h4><span>Consultant</span></div>
  <div class="member" style="left:612px"><div class="portrait" role="img" aria-label="Portrait of Omar Haddad" style="background:radial-gradient(ellipse 30% 22% at 50% 32%, rgba(160,115,85,.9), transparent 70%),linear-gradient(180deg,#f3f3f3 0%,#e8e8e8 50%,#1e2024 72%,#15161a 100%)"></div><h4>OMAR HADDAD</h4><span>Consultant</span></div>
  <div class="member" style="left:836px"><div class="portrait" role="img" aria-label="Portrait of Sara Lind" style="background:radial-gradient(ellipse 36% 26% at 50% 32%, rgba(228,200,170,.9), transparent 72%),linear-gradient(180deg,#f6f6f6 0%,#efefef 55%,#d9d2c8 78%,#c8bfb2 100%)"></div><h4>SARA LIND</h4><span>Photographer</span></div>
</section>

<section class="map" role="img" aria-label="Street map showing the office location"></section>

<section class="contact">
  <div class="photo photo-papers" role="img" aria-label="Desk with papers and a pen in low light"></div>
  <div class="veil"></div>
  <h2 class="section-title">CONTACT US TODAY</h2>
  <div class="field" style="top:298px;left:165px;width:275px;height:40px">Name</div>
  <div class="field" style="top:298px;left:465px;width:275px;height:40px">Email</div>
  <div class="field" style="top:298px;left:765px;width:275px;height:40px">Phone</div>
  <div class="field" style="top:357px;left:165px;width:875px;height:105px">Message</div>
  <div class="submit">SUBMIT</div>
</section>

<footer class="site-footer">
  <span>© 2017 K7P Ledger &amp; Consulting. All Right Reserved.</span>
  <span class="brand">K7P Ledger &amp; Consulting</span>
</footer>

</body>
</html>
```